Introduction of new dentist and new treatments

We want inform our Patients of our new dentist and new treatment methods. It is dealing about biologic dentistry and holistic dentistry. we are in switzerland and speak german

Font styles to use
Sans Serif

Colors
00a990
33b8a4
9bcb3c
acd036
cadf82
0292cd
3176b5
e34297
e667a6

Requirements
Must have
• Text, which can be edited. It will be in german
• Name of the dental clinic is
• "Brivana - Ihr Zahnarzt in Zug"
Nice to have
• A4 Layout

```html
<!DOCTYPE html>
<html lang="de">
<head>
<meta charset="utf-8">
<title>Brivana – Ihr Zahnarzt in Zug</title>
<link href="https://fonts.googleapis.com/css2?family=Ubuntu:wght@400;500;700&family=Tinos&display=swap" rel="stylesheet">
<style>
  :root{
    --navy:#1c3a66;
    --blue:#1f6fb8;
    --sky:#0292cd;
    --green:#3fb54a;
    --green-light:#9bcb3c;
    --wave-blue:#a9dbe6;
    --paper:#eef6f7;
    --text:#4a4f57;
    --white:#ffffff;
  }
  *{margin:0;padding:0;box-sizing:border-box}
  html,body{width:971px;height:1200px;overflow:hidden;background:var(--paper)}
  .flyer{position:relative;width:971px;height:1200px;background:var(--paper);font-family:"Ubuntu",sans-serif;color:var(--text)}
  .hero{position:absolute;left:0;top:0;width:971px;height:520px}
  .brand{position:absolute;left:25px;top:394px}
  .brand-name{font-size:40px;font-weight:500;letter-spacing:11px;color:var(--navy);line-height:1}
  .brand-tagline{margin:14px 0 0 70px;font-size:18px;font-weight:500;color:var(--navy)}
  .headline{position:absolute;left:0;top:532px;width:971px;text-align:center;font-family:"Tinos",serif;font-size:26px;line-height:31px;color:var(--blue);font-weight:400}
  .lead{position:absolute;left:48px;top:606px;width:880px;font-size:15.5px;line-height:21px;color:var(--navy);font-weight:500}
  .topic{position:absolute;width:446px}
  .topic-head{display:flex;align-items:center;gap:10px;height:36px;margin-bottom:6px}
  .topic-icon{width:40px;height:36px;flex:none}
  .topic-title{font-size:16px;line-height:17px;color:var(--navy);font-weight:400}
  .topic-body{font-size:13.2px;line-height:15.6px;text-align:justify;hyphens:auto}
  .t1{left:25px;top:682px}
  .t2{left:500px;top:680px}
  .t3{left:25px;top:887px}
  .t4{left:500px;top:887px}
  .contact{position:absolute;left:0;top:1115px;width:971px;height:85px;background:var(--navy);color:var(--white);display:flex;align-items:center;justify-content:space-between;padding:0 32px 0 25px;font-size:16px}
  .contact-item{display:flex;align-items:center;gap:9px}
  .contact-item svg{width:18px;height:18px;flex:none}
</style>
</head>
<body>
<div class="flyer">
  <svg class="hero" viewBox="0 0 971 520" xmlns="http://www.w3.org/2000/svg">
    <defs>
      <linearGradient id="photoTone" x1="0" y1="0" x2="1" y2="1">
        <stop offset="0" stop-color="#b9c98e"/>
        <stop offset="0.35" stop-color="#e9c9a6"/>
        <stop offset="0.7" stop-color="#f0d6b8"/>
        <stop offset="1" stop-color="#c7d7a0"/>
      </linearGradient>
      <linearGradient id="portraitTone" x1="0" y1="0" x2="0" y2="1">
        <stop offset="0" stop-color="#f2f4f4"/>
        <stop offset="0.6" stop-color="#e3c2a8"/>
        <stop offset="1" stop-color="#1f67b3"/>
      </linearGradient>
    </defs>
    <rect x="0" y="0" width="971" height="470" fill="url(#photoTone)" role="img" aria-label="Foto einer lachenden Familie mit Grosseltern, Eltern und Kindern im Freien"/>
    <path d="M0,240 C170,195 360,210 450,305 C505,362 545,405 610,428 L0,505 Z" fill="var(--white)"/>
    <path d="M0,245 C160,215 300,215 380,250" fill="none" stroke="#dfe6ea" stroke-width="6" opacity="0.7"/>
    <path d="M0,478 C260,505 500,470 720,430 C820,413 900,402 971,398 L971,520 L0,520 Z" fill="var(--paper)"/>
    <path d="M0,490 C260,518 500,482 720,442 C820,424 900,412 971,408 L971,422 C900,428 820,440 720,458 C500,498 260,532 0,504 Z" fill="var(--wave-blue)"/>
    <path d="M0,478 C260,505 500,470 720,430 C820,413 900,402 971,398 L971,412 C900,416 820,428 720,446 C500,486 250,518 0,492 Z" fill="var(--green)"/>
    <circle cx="832" cy="412" r="106" fill="#9fd58f"/>
    <circle cx="832" cy="412" r="92" fill="url(#portraitTone)" role="img" aria-label="Porträtfoto des neuen Zahnarztes im blauen Poloshirt"/>
  </svg>

  <div class="brand">
    <div class="brand-name">BRIVANA</div>
    <div class="brand-tagline">Ihre Zahnärzte in Zug</div>
  </div>

  <h1 class="headline">Interdisziplinäre Zahnmedizin - Zusammenhang zwischen Zahnproblemen<br>und der Gesundheit von Körper und Geist</h1>

  <p class="lead">Zahn und Gesundheit haben eins gemeinsam – Man vermisst sie, wenn sie fehlt. Zähne haben einen engen Zusammenhang zur Gesundheit und können diese beeinflussen. Sowohl negativ als auch positiv.</p>

  <section class="topic t1">
    <div class="topic-head">
      <svg class="topic-icon" viewBox="0 0 40 36"><circle cx="22" cy="14" r="10" fill="none" stroke="var(--green)" stroke-width="3.5"/><path d="M14,21 L4,32" stroke="var(--green)" stroke-width="5" stroke-linecap="round"/><path d="M26,6 c4,0 8,3 7,9 c-1,5 -2,12 -4,12 c-2,0 -2,-5 -3,-5 c-1,0 -1,5 -3,5 c-2,0 -3,-7 -4,-12 c-1,-6 3,-9 7,-9z" fill="var(--sky)"/></svg>
      <h2 class="topic-title">Funktion des Kauorgans<br>und interdisziplinäre Zahnmedizin</h2>
    </div>
    <p class="topic-body">„Funktion ist nicht alles. Aber ohne Funktion ist alles nichts!“ Sagte einst Prof.L.Weidmann(Zahnarzt, Gnathologie) und betonte die Bedeutung der Funktion des Kausystems. Sprechen, Kauen aber auch Körperhaltung und Stressmanagement gehören zu den Funktionen der Zähne. Ein gut funktionierendes Kauorgan (nach Prof.M. Haldner, interdisziplinäre Zahnmedizin) kann Stress bewältigen und mehr Leistung und Wohlbefinden bringen. Sehr oft erkennt man Funktionsstörungen daran, dass die Zähne nicht richtig zueinander passen oder Muskelverspannungen und Schmerzen im Kiefergelenk auftreten.</p>
  </section>

  <section class="topic t2">
    <div class="topic-head">
      <svg class="topic-icon" viewBox="0 0 40 36"><path d="M4,34 L4,20 c5,2 10,2 14,-2 l0,16z M22,18 c4,4 9,4 14,2 l0,14 l-14,0z" fill="var(--green)"/><path d="M18,2 c4,0 8,2 7,8 c-1,5 -2,9 -4,9 c-2,0 -2,-4 -3,-4 c-1,0 -1,4 -3,4 c-2,0 -3,-4 -4,-9 c-1,-6 3,-8 7,-8z" fill="var(--sky)"/></svg>
      <h2 class="topic-title">Parodontitis und<br>systemische Erkrankungen</h2>
    </div>
    <p class="topic-body">Parodontitis (Entzündung des Zahnhalteapparats) ist eine der häufigsten chronischen Krankheiten weltweit und daher gut erforscht. Herzkrankheiten, Diabetes und Frühgeburtlichkeit sind einige der systemischen Krankheiten mit der Parodontitis in Zusammenhang steht.Zahnfleischbluten, Zahnlockerung, Zahnfleischschwund und Zahnverlust sind typische Begleiterscheinungen von Parodontitis. Eine systematische Parodontitis-Behandlung kann auchpositive Auswirkungen auf die gesamte Gesundheit haben.</p>
  </section>

  <section class="topic t3">
    <div class="topic-head">
      <svg class="topic-icon" viewBox="0 0 40 36"><path d="M20,2 c6,0 11,3 10,11 c-1,8 -3,21 -6,21 c-3,0 -2,-9 -4,-9 c-2,0 -1,9 -4,9 c-3,0 -5,-13 -6,-21 c-1,-8 4,-11 10,-11z" fill="var(--sky)"/></svg>
      <h2 class="topic-title">Zahnverlust und<br>neurologische Auswirkung</h2>
    </div>
    <p class="topic-body">Ein physiologisches Kausystem hat sehr feine Steuerungs- und Wahrnehmungsmöglichkeiten. Bei Zahnverlust werden diese Fähigkeiten weniger benötigt. Weniger gebrauchte Ressourcen werden von der Natur dementsprechend abgebaut. Studien zeigen, dass Menschen mit weniger Zähnen mehr Risiko zur Bildung von Demenz bergen.</p>
  </section>

  <section class="topic t4">
    <div class="topic-head">
      <svg class="topic-icon" viewBox="0 0 40 36"><path d="M20,10 c6,-4 15,-2 15,9 c0,9 -7,16 -11,16 c-2,0 -3,-1 -4,-1 c-1,0 -2,1 -4,1 c-4,0 -11,-7 -11,-16 c0,-11 9,-13 15,-9z" fill="var(--sky)"/><path d="M20,10 c0,-5 3,-8 8,-9 c0,5 -3,8 -8,9z" fill="var(--green)"/></svg>
      <h2 class="topic-title">Ganzheitliche Erklärungen</h2>
    </div>
    <p class="topic-body">Die komplementäre Zahnheilkunde, sehr oft auch als ganzheitliche oder biologische Zahnheilkunde bezeichnet, versucht mit Hilfe von Meridianen(Traditionelle Chinesische Medizin), den Zusammenhang zwischen Zähnen und anderen Organen und Körperteilen zu erklären. Es gibt immer mehr Patienten und Zahnärzte die von dieser Theorie und deren Ergebnissen überzeugt sind. Aufgrund der wissenschaftlichen Lage ist eine ausführliche Aufklärung vor der Behandlung sehr ratsam.</p>
  </section>

  <footer class="contact">
    <div class="contact-item">
      <svg viewBox="0 0 18 18"><path d="M9,1 c3.5,0 6,2.6 6,6 c0,4 -6,10 -6,10 c0,0 -6,-6 -6,-10 c0,-3.4 2.5,-6 6,-6z" fill="var(--white)"/><circle cx="9" cy="7" r="2.2" fill="var(--navy)"/></svg>
      <span>Zahnarztpraxis Seestrasse 14, 6300 Zug</span>
    </div>
    <div class="contact-item">
      <svg viewBox="0 0 18 18"><circle cx="9" cy="9" r="7.5" fill="none" stroke="var(--white)" stroke-width="1.5"/><path d="M6,5 l1.5,0 l0.8,2 l-1,1 c0.6,1.3 1.4,2.1 2.7,2.7 l1,-1 l2,0.8 l0,1.5 c-4,0.5 -7.5,-3 -7,-7z" fill="var(--white)"/></svg>
      <span>+41 41 000 12 34</span>
    </div>
    <div class="contact-item">
      <svg viewBox="0 0 18 18" fill="none" stroke="var(--white)" stroke-width="1.3"><circle cx="9" cy="9" r="7.5"/><ellipse cx="9" cy="9" rx="3.3" ry="7.5"/><path d="M1.5,9 h15 M2.8,5 h12.4 M2.8,13 h12.4"/></svg>
      <span>www.brivana-zug.ch</span>
    </div>
  </footer>
</div>
</body>
</html>
```